Following list to be designed:

1. A4 Letter Head

Must comprise of:
BRISK HARBOR and its LOGO
Address: No.41, 2F, Telvin Court, Marlow Lane, Upper Fennel Gardens, Bangalore 560 078
Tel: 080 41927380
Fax: 080 41927381
Mail: hello@briskharbor.example

Color of wordings to be in the lighter shade of blue and brighter shade of blue.

2. A4 Envelope

Must comprise of:
BRISK HARBOR and its LOGO
Tel: 080 41927380
Fax: 080 41927381

3. Postal Envelope

Must comprise of:
BRISK HARBOR and its LOGO
Tel: 080 41927380
Fax: 080 41927381

4. Business Card

Must comprise of:
Ravi Menon
Managing Partner
Cell: +91 9847162053
Mail: ravimenon@briskharbor.example
Tel: 080 41927380
Fax: 080 41927381

5. A4 Letter Head

Must comprise of:
BRISK HARBOR CORP. (wording) and BRISK HARBOR LOGO (only blue ribbon)

Blue ribbon (BRISK HARBOR LOGO) may be placed on Left Top Corner of the A4 Letter Head
and BRISK HARBOR CORP. (wording) to be placed on Right Top Corner of the A4 Letter Head

Tel: 080 41927380
Fax: 080 41927381

6. . A4 Envelope

Must comprise of:

Blue ribbon (BRISK HARBOR LOGO) may be placed on Left Top Corner of the A4 Envelope
and BRISK HARBOR CORP. (wording) to be placed on Right Top Corner of the A4 Envelope
Tel: 080 41927380
Fax: 080 41927381

Target Market(s)

Top IT/ITES Organizations

Industry/Entity Type

Real Estate Development

Font styles to use
Serif
Sans Serif

Colors
33a6d7
0792cd
85cae6

Requirements
Should not have
• Playful font and color

```html
<!DOCTYPE html>
<html lang="en">
<head>
<meta charset="utf-8">
<title>Brisk Harbor — Stationery Set</title>
<link href="https://fonts.googleapis.com/css2?family=Montserrat:wght@500;600&family=Open+Sans:wght@400;600&display=swap" rel="stylesheet">
<style>
  :root{
    --bg:#a3a3a3;
    --paper:#f2f2f3;
    --paper-edge:#dcdcde;
    --brand:#1d5ea8;
    --brand-dark:#16467f;
    --bright:#0792cd;
    --sky:#33a6d7;
    --pale:#85cae6;
    --ink:#3d4a5a;
    --grey-word:#6e6f68;
    --white:#ffffff;
  }
  *{margin:0;padding:0;box-sizing:border-box}
  html,body{width:1200px;height:1200px;overflow:hidden}
  body{background:var(--bg);position:relative;font-family:"Open Sans",Arial,sans-serif;color:var(--ink)}

  .brand-name{font-family:"Montserrat",Arial,sans-serif;font-weight:500;color:var(--brand);letter-spacing:.02em;white-space:nowrap}
  .lockup{display:flex;align-items:center;gap:10px}
  .lockup .mark{background:var(--sky);flex:none}

  .hero-lockup{position:absolute;left:40px;top:48px}
  .hero-lockup .mark{width:58px;height:58px}
  .hero-lockup .brand-name{font-size:44px;color:var(--grey-word)}

  .sheet{position:absolute;background:var(--paper);box-shadow:0 2px 6px rgba(0,0,0,.22)}

  .letterhead{width:280px;height:396px;top:170px}
  .letterhead--ribbon{left:40px}
  .letterhead--classic{left:350px}

  .ribbon-mark{position:absolute;left:20px;top:20px;width:34px;height:34px;background:var(--bright)}
  .letterhead--ribbon .brand-name{position:absolute;right:20px;top:30px;font-size:15px}
  .letterhead--classic .lockup{position:absolute;left:20px;top:22px}
  .letterhead--classic .mark{width:26px;height:26px}
  .letterhead--classic .brand-name{font-size:15px}

  .contact-footer{position:absolute;right:18px;bottom:18px;text-align:right;font-size:6.4px;line-height:1.6;color:var(--ink);white-space:nowrap}
  .contact-row{display:flex;justify-content:flex-end;gap:8px;align-items:center}
  .contact-item{display:inline-flex;align-items:center;gap:3px}
  .icon{display:inline-block;width:6px;height:6px;background:var(--brand);flex:none}

  .envelope-dl{left:660px;top:170px;width:500px;height:250px}
  .envelope-dl .lockup{position:absolute;left:26px;top:28px}
  .envelope-dl .mark{width:34px;height:34px}
  .envelope-dl .brand-name{font-size:20px}
  .envelope-dl .contact-footer{right:26px;bottom:26px;font-size:8px}
  .envelope-dl .icon{width:7px;height:7px}

  .envelope-a4{left:40px;top:620px;width:600px;height:424px;overflow:hidden}
  .envelope-a4 .flap{position:absolute;left:0;top:0;width:100%;height:56px;background:linear-gradient(90deg,var(--brand-dark),var(--brand) 55%,var(--bright));display:flex;align-items:center;justify-content:center}
  .envelope-a4 .flap .lockup{gap:8px}
  .envelope-a4 .flap .mark{width:18px;height:18px;background:var(--pale)}
  .envelope-a4 .flap .brand-name{font-size:14px;color:var(--pale)}
  .envelope-a4 .flap-fold{position:absolute;left:0;top:56px;width:100%;height:3px;background:var(--paper-edge)}
  .envelope-a4 .ribbon-mark{left:28px;top:84px;width:40px;height:40px}
  .envelope-a4 .corp-name{position:absolute;right:28px;top:96px;font-size:18px}
  .envelope-a4 .contact-footer{right:28px;bottom:26px;font-size:8px}
  .envelope-a4 .icon{width:7px;height:7px}

  .card{width:250px;height:150px;top:450px}
  .card--back{left:910px;background:radial-gradient(circle at 50% 45%,var(--sky),var(--brand) 75%)}
  .card--front{left:660px}
  .card-person{position:absolute;right:16px;top:16px;width:150px}
  .card-person .person-name{font-family:"Montserrat",Arial,sans-serif;font-weight:600;font-size:12px;color:var(--brand)}
  .card-person .person-role{font-size:7px;color:var(--ink);margin-bottom:5px}
  .card-person .card-line{font-size:6px;line-height:1.55;display:flex;align-items:center;gap:4px}
  .card--front .lockup{position:absolute;left:14px;bottom:14px;gap:6px}
  .card--front .mark{width:18px;height:18px}
  .card--front .brand-name{font-size:10px}
</style>
</head>
<body>

  <div class="lockup hero-lockup">
    <span class="mark"></span>
    <span class="brand-name">BRISK HARBOR</span>
  </div>

  <section class="sheet letterhead letterhead--ribbon" aria-label="Letterhead with ribbon">
    <span class="ribbon-mark"></span>
    <span class="brand-name">BRISK HARBOR CORP.</span>
    <div class="contact-footer">
      <div class="contact-row">
        <span class="contact-item"><span class="icon"></span>080 41927380</span>
        <span class="contact-item"><span class="icon"></span>080 41927381</span>
      </div>
    </div>
  </section>

  <section class="sheet letterhead letterhead--classic" aria-label="Letterhead">
    <div class="lockup"><span class="mark"></span><span class="brand-name">BRISK HARBOR</span></div>
    <div class="contact-footer">
      <div>No.41, 2F, Telvin Court, Marlow Lane, Upper Fennel Gardens, Bangalore 560 078</div>
      <div class="contact-row">
        <span class="contact-item"><span class="icon"></span>080 41927380</span>
        <span class="contact-item"><span class="icon"></span>080 41927381</span>
        <span class="contact-item"><span class="icon"></span>hello@briskharbor.example</span>
      </div>
    </div>
  </section>

  <section class="sheet envelope-dl" aria-label="Postal envelope">
    <div class="lockup"><span class="mark"></span><span class="brand-name">BRISK HARBOR</span></div>
    <div class="contact-footer">
      <div>No.41, 2F, Telvin Court, Marlow Lane, Upper Fennel Gardens, Bangalore 560 078</div>
      <div class="contact-row">
        <span class="contact-item"><span class="icon"></span>080 41927380</span>
        <span class="contact-item"><span class="icon"></span>080 41927381</span>
        <span class="contact-item"><span class="icon"></span>hello@briskharbor.example</span>
      </div>
    </div>
  </section>

  <section class="sheet card card--front" aria-label="Business card front">
    <div class="card-person">
      <div class="person-name">Ravi Menon</div>
      <div class="person-role">Managing Partner</div>
      <div class="card-line">No.41, 2F, Telvin Court, Marlow Lane, Upper Fennel Gardens, Bangalore 560 078</div>
      <div class="card-line"><span class="icon"></span>+91 9847162053</div>
      <div class="card-line"><span class="icon"></span>080 41927380</div>
      <div class="card-line"><span class="icon"></span>080 41927381</div>
      <div class="card-line"><span class="icon"></span>ravimenon@briskharbor.example</div>
    </div>
    <div class="lockup"><span class="mark"></span><span class="brand-name">BRISK HARBOR</span></div>
  </section>

  <section class="sheet card card--back" aria-label="Business card back"></section>

  <section class="sheet envelope-a4" aria-label="A4 envelope">
    <div class="flap">
      <div class="lockup"><span class="mark"></span><span class="brand-name">BRISK HARBOR</span></div>
    </div>
    <div class="flap-fold"></div>
    <span class="ribbon-mark"></span>
    <span class="brand-name corp-name">BRISK HARBOR CORP.</span>
    <div class="contact-footer">
      <div class="contact-row">
        <span class="contact-item"><span class="icon"></span>080 41927380</span>
        <span class="contact-item"><span class="icon"></span>080 41927381</span>
      </div>
    </div>
  </section>

</body>
</html>
```